Tallbrook Meridian Advisory needs business cards

Tallbrook Meridian Advisory is a new approach to consulting: we believe in partnering our clients in a hands-on, side-by-side, rolling-up-our sleeves approach, rather than being removed and aloof consultants.

We have a logo design developped through PixelHarbor (see attachment) and need to move to the stage of designing a business card for our 7 founding members.

Target Market(s)

Senior executives in local and global companies (such as Fizzmont Tonic, Hollanby, Brevard, etc)

Industry/Entity Type

Business

Requirements
Must have
• Look and feel: The design reflect the logo: i.e. professional, modern and approachable (as opposed to corporate traditional and remote). We are looking for a high quality, premium design.

Content must haves:
- prominent: our logo, person's name, function, phone number and e-mail address
- less prominent: company address and website

Example: Tallbrook Meridian Advisory logo, Mireille Vostag, Partner, +44 (0)781 209 3375, mireille_vostag@tallbrookmeridian.example / 17 Pelham Crescent, Esher, Surrey, UK, KT10 3WN - www.tallbrookmeridian.example

- Both sides of the card can be used
- Both versions of the logo can be used (on black or on white)

```html
<!DOCTYPE html>
<html lang="en">
<head>
<meta charset="utf-8">
<title>Tallbrook Meridian Advisory – Business Card</title>
<link rel="stylesheet" href="https://fonts.googleapis.com/css2?family=PT+Sans:ital,wght@0,400;0,700;1,400;1,700&family=Fira+Sans+Condensed:ital,wght@1,400&display=swap">
<style>
  :root {
    --brand-blue: #1a8fd0;
    --ink: #2e2e2e;
    --ink-soft: #4a4a4a;
    --paper: #ffffff;
    --glow: #d6ebf7;
  }
  html, body {
    margin: 0;
    padding: 0;
    width: 1200px;
    height: 777px;
    overflow: hidden;
    background: var(--paper);
  }
  .card {
    position: relative;
    width: 1200px;
    height: 777px;
    background: var(--paper);
    font-family: "PT Sans", "Helvetica Neue", Arial, sans-serif;
    overflow: hidden;
  }
  .corner-accent {
    position: absolute;
    right: -60px;
    top: -120px;
    width: 420px;
    height: 390px;
    border-radius: 50%;
    background: radial-gradient(ellipse at 45% 55%, var(--glow) 0%, rgba(214,235,247,0.55) 40%, rgba(255,255,255,0) 70%);
  }
  .person {
    position: absolute;
    left: 72px;
    top: 128px;
  }
  .person__name {
    margin: 0;
    font-size: 46px;
    font-weight: 700;
    color: var(--brand-blue);
    letter-spacing: 0.01em;
    line-height: 1;
  }
  .person__role {
    margin: 8px 0 0;
    font-size: 34px;
    font-style: italic;
    color: var(--brand-blue);
    line-height: 1;
  }
  .contact {
    position: absolute;
    left: 72px;
    top: 318px;
    margin: 0;
    font-size: 27px;
    color: var(--ink);
    letter-spacing: 2px;
    line-height: 44px;
    font-style: normal;
  }
  .divider {
    position: absolute;
    left: 769px;
    top: 136px;
    width: 4px;
    height: 572px;
    background: var(--brand-blue);
  }
  .brand {
    position: absolute;
    left: 72px;
    top: 540px;
    display: flex;
    align-items: center;
    gap: 22px;
  }
  .brand__dot {
    width: 150px;
    height: 150px;
    border-radius: 50%;
    background: var(--brand-blue);
    flex: none;
  }
  .brand__name {
    font-size: 38px;
    font-weight: 700;
    color: var(--ink);
    line-height: 1.05;
  }
  .office {
    position: absolute;
    left: 800px;
    right: 72px;
    top: 568px;
    text-align: right;
    font-family: "Fira Sans Condensed", "PT Sans", Arial, sans-serif;
    font-style: italic;
    white-space: nowrap;
  }
  .office__address {
    margin: 0;
    font-size: 26px;
    color: var(--ink-soft);
    line-height: 46px;
  }
  .office__web {
    margin: 10px 0 0;
    font-size: 21px;
    letter-spacing: 1px;
    line-height: 30px;
    color: var(--brand-blue);
  }
</style>
</head>
<body>
  <main class="card">
    <div class="corner-accent" role="img" aria-label="Faint blue brand swirl decoration"></div>

    <header class="person">
      <h1 class="person__name">Mireille Vostag</h1>
      <p class="person__role">Partner</p>
    </header>

    <address class="contact">
      +44 (0)781 209 3375<br>
      mireille_vostag@tallbrookmeridian.example
    </address>

    <div class="divider"></div>

    <div class="brand">
      <div class="brand__dot"></div>
      <div class="brand__name">Tallbrook Meridian<br>Advisory</div>
    </div>

    <div class="office">
      <p class="office__address">
        17 Pelham Crescent,<br>
        Esher, Surrey, UK, KT10 3WN
      </p>
      <p class="office__web">www.tallbrookmeridian.example</p>
    </div>
  </main>
</body>
</html>
```